Flyer Design Project

Our company focuses on selling Consumer products like home furniture, home decor, electronics and accessories by public auction. We need a flyer design that will showcase these products with pictures and text. Illustration and desciption on the flyer is always genetic and never changes, The flyer design should be simple and straight forward with limited graphic design and instead focus on product description and emphasise on words Public Auction, and the word AUCTION being the main heading on the flyer. Multilpe colours are prefered.

Target Market(s)

Age group between 30-65 lmajority living in rural, homeowners and looking for a great quality product at an economical price

Industry/Entity Type

Graphic Design

Requirements
Must have
• The flyer should be tri-fold 11x17 inches in size fron and back.
Nice to have
• To show consumers that they have an opportunity to save money by attending our auctions.
Should not have
• The flyer design should not look too corporate or sophisticated. Simple approach to target consumers since most of them live in rural areas.

```html
<!DOCTYPE html>
<html lang="en">
<head>
<meta charset="utf-8">
<title>Public Auction Flyer</title>
<link rel="stylesheet" href="https://fonts.googleapis.com/css2?family=Arimo:wght@400;700&family=Anton&family=Cinzel:wght@400;700&display=swap">
<style>
  :root {
    --white: #ffffff;
    --yellow-bright: #fff200;
    --yellow-deep: #f3cd11;
    --headline-yellow: #f1cf10;
    --pink: #e6157f;
    --teal: #5b9c93;
    --ink: #111111;
    --logo-grey: #6b7478;
    --photo-top: #8a3a2e;
    --photo-bottom: #4a3226;
  }
  * { box-sizing: border-box; margin: 0; padding: 0; }
  html, body { width: 1200px; height: 618px; overflow: hidden; background: var(--white); }
  .flyer {
    position: relative; width: 1200px; height: 618px; overflow: hidden;
    font-family: "Arimo", Arial, sans-serif; color: var(--ink); background: var(--white);
  }
  .band { position: absolute; top: 0; height: 618px; }
  .band--mid-edge { left: 342px; width: 453px; background: var(--yellow-deep); }
  .band--mid { left: 368px; width: 402px; background: var(--yellow-bright); }
  .band--right { left: 1148px; width: 52px; background: var(--yellow-deep); }

  .brand { position: absolute; left: 12px; top: 34px; display: flex; align-items: center; gap: 12px; }
  .brand__dot { width: 36px; height: 36px; border-radius: 50%; background: var(--teal); }
  .brand__name { font-weight: 700; font-size: 27px; line-height: 30px; color: var(--logo-grey); letter-spacing: 0.5px; }

  .tagline { position: absolute; left: 8px; top: 124px; font-size: 12px; }
  .departments { position: absolute; left: 8px; top: 148px; list-style: none; font-weight: 700; font-size: 13px; line-height: 17px; }

  .savings { position: absolute; right: 874px; top: 336px; text-align: right; color: var(--pink); font-weight: 700; font-size: 19px; line-height: 27px; }
  .headline { position: absolute; right: 870px; top: 420px; text-align: right; font-family: "Anton", Impact, sans-serif; color: var(--headline-yellow); font-size: 68px; line-height: 66px; letter-spacing: 1px; }
  .clearout { position: absolute; left: 4px; top: 559px; color: var(--teal); font-weight: 700; font-size: 18.5px; letter-spacing: 0.2px; }

  .bubble { position: absolute; left: 605px; top: 14px; width: 190px; height: 110px; }
  .bubble__text { position: absolute; left: 613px; top: 45px; width: 170px; text-align: center; color: var(--white); font-weight: 700; font-size: 15px; line-height: 20px; }

  .auctioneer { position: absolute; left: 416px; top: 87px; font-weight: 700; font-size: 13px; line-height: 17px; }
  .inventory {
    position: absolute; left: 380px; top: 160px; width: 400px; list-style: none;
    text-align: center; font-weight: 700; font-size: 10px; line-height: 13.75px; white-space: nowrap;
  }

  .showcase { position: absolute; left: 868px; top: 38px; width: 250px; height: 305px; border-radius: 40px 40px 10px 10px; background: linear-gradient(160deg, var(--photo-top), var(--photo-bottom)); }
  .selection { position: absolute; left: 800px; top: 358px; width: 345px; text-align: center; font-weight: 700; }
  .selection__title { font-size: 18px; line-height: 22px; }
  .selection__sub { font-size: 12px; line-height: 18px; }
  .selection__delivery { color: var(--pink); font-size: 18.5px; line-height: 34px; letter-spacing: 0.3px; }

  .invite { position: absolute; left: 800px; top: 520px; width: 345px; text-align: center; font-family: "Cinzel", Georgia, serif; }
  .invite__fun { color: var(--teal); font-size: 25px; line-height: 34px; }
  .invite__cta { color: var(--headline-yellow); font-weight: 700; font-size: 31px; line-height: 40px; }
</style>
</head>
<body>
<main class="flyer">
  <div class="band band--mid-edge"></div>
  <div class="band band--mid"></div>
  <div class="band band--right"></div>

  <header class="brand">
    <span class="brand__dot"></span>
    <span class="brand__name">HARVEST<br>LIQUIDATORS</span>
  </header>
  <p class="tagline">OVER A MILION DOLLARS MAJOR LIQUIDATION</p>
  <ul class="departments">
    <li>NEW FINE FURNITURE</li>
    <li>HOME DECOR</li>
    <li>ELECTRONICS &amp; ACCESSORIES</li>
  </ul>

  <p class="savings">Load Up Huge<br>on Savings at the</p>
  <h1 class="headline">PUBLIC<br>AUCTION</h1>
  <p class="clearout">MASSIVE INVENTORY CLEAROUT</p>

  <svg class="bubble" viewBox="0 0 190 110" aria-hidden="true">
    <path d="M93 5 C140 5 178 25 178 52 C178 79 140 98 93 98 C80 98 68 97 57 94 L34 108 L42 88 C20 80 8 67 8 52 C8 25 46 5 93 5 Z" fill="var(--pink)"/>
  </svg>
  <p class="bubble__text">EVERYTHING<br>MUST SELL</p>

  <p class="auctioneer">Dale Hartley, auctioneer<br>has been authorized to liquidate<br>the following inventory</p>

  <ul class="inventory">
    <li>Bedroom suits to include mission, platform, sleigh and poster beds</li>
    <li>in queen Anne, Victorian, Louis Phillip, and French accented designs</li>
    <li>in Queen and King Sizes,</li>
    <li>Large variety of high quality 3-piece sofa sets from Italian leather</li>
    <li>to design fabric in various styles and colours</li>
    <li>(Black, Taupe, Burgundy, Red Wine, Chocolate, Stone Gey &amp; Whisky)</li>
    <li>Stunning dinning room suits also to include pub and dinette sets</li>
    <li>in mahogany, walnut, oak, and cherry,</li>
    <li>High quality (made in Canada)orthopedic pillow top mattress sets</li>
    <li>in Queen and King size</li>
    <li>Various home decor items including lamps, wall mirrors, TV stands, etc.</li>
    <li>Storage ottomans, Various Occassional tables, coffee and E</li>
    <li>End tables sets</li>
    <li>China and curio cabinets</li>
    <li>Corner tables, sofa tables,</li>
    <li>High quality imported area rugs in several, sizes, patterns, and colours</li>
    <li>31-day grandfather clocks</li>
    <li>Selection of brand name LCD &amp; Plasma HDTV's DVD Blue Ray players</li>
    <li>Home theater suround sound systems,</li>
    <li>Diverse selection of Collctors Artwork for investment</li>
    <li>by known &amp; respected canadian artists</li>
    <li>Earings &amp; neckless</li>
    <li>Nostalgia items,</li>
    <li>Decorative wases</li>
    <li>18/10 stainless stell cookware sets</li>
    <li>knife sets with block. culery stes with display cases</li>
    <li>Raplica guns w/ shadobox dispaly cases</li>
    <li>Diecast model cars</li>
    <li>Various, collectible figurines</li>
    <li>Large wall clocks</li>
    <li>Various decorative signs &amp; display cases</li>
    <li>Model ships</li>
  </ul>

  <div class="showcase" role="img" aria-label="Photo of a man carrying a stack of furniture: leather sofa, red armchair, dining chairs, table and rolled rug"></div>

  <section class="selection">
    <p class="selection__title">A HUGE selection!</p>
    <p class="selection__sub">offering variety quality &amp; quantity</p>
    <p class="selection__delivery">DELIVERY AVAILABLE</p>
  </section>

  <section class="invite">
    <p class="invite__fun">COME OUT, HAVE FUN</p>
    <p class="invite__cta">DON’T MISS IT!</p>
  </section>
</main>
</body>
</html>
```